Automotive Repair Centre - Flyer Design

Bremwick Motors Cumbernauld are looking for a completely new flyer design for our blossoming auto repair centre. We are looking for bold eye catching designs as these flyers will be letterbox dropped around the local community. Approx. 10k per month. These will be printed double sided, on A5, with different print front and rear. Currently the whole rear is dedicated to servicing only, but this can be changed.

Our business prides itself on providing a high quality service so they flyer needs to convey this message. Also we believe in fair prices so they flyer also needs to convey this message in the design. Colour scheme is currently blue, yellow, and black. If possible it would be good to include the Drivemarq logo and the KELP logo.

We like the "specials" list from the Halvorn Drake flyer that is attached. We also like the clean look and layout of the other flyer that is uploaded. It would be good to include a special area for winter tyres much like is shown in the 50% off wheel alignment piece of the flyer attached.

Our current flyer uses the font GoodTimes as we would like this to remain if possible. It can be changed if the designer prefers. You can visit our website www.bremwick.co.uk for more information about our business.
Updates

Reason: Not had enough good designs to choose from yet.

Reason: Still not enough good designs to choose from

Reason: designs not up to the standard required.

Reason: Not enough designs that capture the brief have been submitted

Reason: looking for more designs

Reason: looking for some more bright designs. please read the brief!!!

Reason: same as before

Target Market(s)

General public.

Industry/Entity Type

Wheel

Requirements
Should not have
• We feel the flyer should not have photos of high end vehicles like Zantellis etc as the does not fit our approach of good value.

```html
<!DOCTYPE html>
<html lang="en">
<head>
<meta charset="utf-8">
<title>Bremwick Motors – Fixed Price Service Flyer</title>
<link rel="stylesheet" href="https://fonts.googleapis.com/css2?family=Michroma&family=Caveat:wght@500&family=Open+Sans:ital,wght@1,700;1,800&display=swap">
<style>
  :root {
    --black: #000000;
    --yellow: #ffe500;
    --white: #ffffff;
    --blue-deep: #0a4d8c;
    --blue-mid: #1f8fd6;
    --blue-light: #5cc4f2;
    --pill-blue: #1a6fc2;
    --swoosh: #d9d9d9;
  }
  * { margin: 0; padding: 0; box-sizing: border-box; }
  html, body { width: 845px; height: 1200px; overflow: hidden; background: var(--black); }
  .flyer {
    position: relative; width: 845px; height: 1200px; overflow: hidden;
    background: var(--black); color: var(--white);
    font-family: "Michroma", "Arial Black", sans-serif;
  }
  .heavy { -webkit-text-stroke: 0.7px currentColor; }
  .backdrop { position: absolute; inset: 0; }
  .abs { position: absolute; }

  .brand { left: 30px; top: 95px; display: flex; align-items: center; gap: 16px; }
  .brand-dot { width: 34px; height: 34px; border-radius: 50%; background: var(--yellow); }
  .brand-name { font-size: 50px; color: var(--white); letter-spacing: 1px; }

  .tagline {
    right: 86px; top: 34px; font-family: "Open Sans", sans-serif; font-style: italic;
    font-weight: 800; font-size: 19px; color: var(--yellow); letter-spacing: 0.5px;
  }
  .tagline .it { color: var(--white); }
  .mechanic {
    right: 86px; top: 70px; font-family: "Open Sans", sans-serif; font-style: italic;
    font-weight: 700; font-size: 11px; color: var(--white);
  }
  .call-pill {
    right: 80px; top: 88px; background: var(--pill-blue); color: var(--white);
    font-family: "Open Sans", sans-serif; font-style: italic; font-weight: 700;
    font-size: 11px; padding: 4px 8px; border-radius: 2px;
  }

  .offer-title { left: 33px; top: 260px; color: var(--yellow); font-size: 30px; white-space: nowrap; font-weight: 400; -webkit-text-stroke: 1.2px currentColor; }
  .offer-title small { font-size: 24px; }
  .offer-sub { left: 152px; top: 303px; font-size: 16px; color: var(--white); white-space: nowrap; }
  .price { left: 30px; top: 348px; color: var(--yellow); font-size: 54px; white-space: nowrap; -webkit-text-stroke: 2px currentColor; }
  .price small { font-size: 19px; margin-left: 16px; -webkit-text-stroke: 0.7px currentColor; }

  .checklist { left: 27px; top: 450px; list-style: none; }
  .checklist li {
    display: flex; align-items: center; gap: 24px; height: 36.8px;
    color: var(--yellow); font-size: 21px; -webkit-text-stroke: 0.8px currentColor;
  }
  .checklist svg { width: 27px; height: 27px; fill: var(--yellow); }

  .photo-circle { position: absolute; border-radius: 50%; border: 4px solid var(--white); }
  .c-repairs { left: 675px; top: 222px; width: 124px; height: 124px; background: radial-gradient(circle, #8a8a8a, #3b3b3b); }
  .c-mot { left: 657px; top: 377px; width: 126px; height: 126px; background: radial-gradient(circle, #6d7f3a, #9a2d2d 55%, #c9c1b5); }
  .c-service { left: 625px; top: 538px; width: 124px; height: 124px; background: radial-gradient(circle, #5573a8, #2a2a2a); }
  .c-tyres { left: 537px; top: 688px; width: 126px; height: 126px; background: radial-gradient(circle, #3a3a3a 30%, #7fd3ea 60%); }

  .service-label { color: var(--white); font-size: 21px; white-space: nowrap; text-shadow: 0 1px 3px rgba(0,0,0,0.6); -webkit-text-stroke: 0.8px currentColor; }
  .l-repairs { left: 541px; top: 271px; }
  .l-mot { left: 447px; top: 426px; }
  .l-service { left: 463px; top: 583px; }
  .l-tyres { left: 415px; top: 744px; }

  .extras { left: 32px; top: 790px; font-size: 15px; line-height: 19.5px; white-space: nowrap; }
  .extras h3, .parts h3 { color: var(--yellow); font-weight: 400; font-size: inherit; }
  .extras p { color: var(--yellow); }
  .parts { left: 32px; top: 890px; font-size: 16px; line-height: 21.5px; white-space: nowrap; }
  .parts h3 { font-size: 16px; margin-bottom: 3px; }
  .parts p { color: var(--white); }

  .advice {
    left: 508px; top: 922px; font-family: "Caveat", cursive; font-weight: 500;
    font-size: 40px; line-height: 38px; color: var(--yellow); white-space: nowrap;
    transform: rotate(-18deg); transform-origin: left top; letter-spacing: 3px;
  }

  .contact { right: 22px; top: 1016px; text-align: right; color: var(--yellow); font-size: 18.5px; line-height: 27px; font-style: normal; white-space: nowrap; }

  .badge { top: 1057px; height: 66px; background: var(--white); }
  .badge-one { left: 20px; width: 213px; }
  .badge-two { left: 248px; width: 214px; }

  .address-band {
    left: 0; top: 1138px; width: 845px; height: 62px; background: var(--yellow);
    color: var(--black); font-size: 17px; display: flex; align-items: center; justify-content: center;
    white-space: nowrap;
  }
</style>
</head>
<body>
<main class="flyer">
  <svg class="backdrop" width="845" height="1200" viewBox="0 0 845 1200">
    <defs>
      <linearGradient id="skyFill" x1="0" y1="0" x2="1" y2="1">
        <stop offset="0" stop-color="#0b5fa8"/>
        <stop offset="0.45" stop-color="#2aa3e3"/>
        <stop offset="1" stop-color="#0a4d8c"/>
      </linearGradient>
    </defs>
    <path d="M0,228 L700,228 C760,420 740,600 640,700 C520,780 300,740 0,780 Z" fill="url(#skyFill)" role="img" aria-label="Photo of a saloon car on a blue sky background"/>
    <path d="M790,0 C800,300 720,600 640,720 C700,860 790,960 845,1010" fill="none" stroke="var(--swoosh)" stroke-width="14"/>
    <path d="M0,780 C200,730 420,720 560,735" fill="none" stroke="var(--white)" stroke-width="3"/>
  </svg>

  <div class="abs brand">
    <span class="brand-dot"></span>
    <span class="brand-name">BREMWICK</span>
  </div>

  <p class="abs tagline">YOU DRIVE <span class="it">IT</span> WE FIX <span class="it">IT</span></p>
  <p class="abs mechanic">I am your mechanic...</p>
  <p class="abs call-pill">Call me: 01236 555014</p>

  <h1 class="abs offer-title">FIXED PRICE <small>SERVICE</small></h1>
  <p class="abs offer-sub heavy">ANY VEHICLE UPTO 2000CC</p>
  <p class="abs price">£89<small>ONLY</small></p>

  <ul class="abs checklist">
    <li><svg viewBox="0 0 24 24"><path d="M12 1l3.1 7.2 7.9.7-6 5.2 1.8 7.7L12 17.8 5.2 21.8 7 14.1 1 8.9l7.9-.7z"/></svg>SPARK PLUG</li>
    <li><svg viewBox="0 0 24 24"><path d="M12 1l3.1 7.2 7.9.7-6 5.2 1.8 7.7L12 17.8 5.2 21.8 7 14.1 1 8.9l7.9-.7z"/></svg>OIL FILTER</li>
    <li><svg viewBox="0 0 24 24"><path d="M12 1l3.1 7.2 7.9.7-6 5.2 1.8 7.7L12 17.8 5.2 21.8 7 14.1 1 8.9l7.9-.7z"/></svg>LONG LIFE OIL</li>
    <li><svg viewBox="0 0 24 24"><path d="M12 1l3.1 7.2 7.9.7-6 5.2 1.8 7.7L12 17.8 5.2 21.8 7 14.1 1 8.9l7.9-.7z"/></svg>AIR FILTER</li>
    <li><svg viewBox="0 0 24 24"><path d="M12 1l3.1 7.2 7.9.7-6 5.2 1.8 7.7L12 17.8 5.2 21.8 7 14.1 1 8.9l7.9-.7z"/></svg>SAFETY CHECK</li>
  </ul>

  <div class="photo-circle c-repairs" role="img" aria-label="Photo of hands working on an engine with a ratchet"></div>
  <div class="photo-circle c-mot" role="img" aria-label="Photo of an MOT diagnostic screen"></div>
  <div class="photo-circle c-service" role="img" aria-label="Photo of a mechanic servicing under a car"></div>
  <div class="photo-circle c-tyres" role="img" aria-label="Photo of a stack of tyres"></div>

  <p class="abs service-label l-repairs">REPAIRS</p>
  <p class="abs service-label l-mot">MOT TESTING</p>
  <p class="abs service-label l-service">SERVICE</p>
  <p class="abs service-label l-tyres">TYRES</p>

  <section class="abs extras heavy">
    <h3>WE ALSO PROVIDE:</h3>
    <p>FAULT DIAGNOSIS | BATTERIES<br>WHEEL ALIGNMENT | WELDING<br>&amp; MORE</p>
  </section>

  <section class="abs parts heavy">
    <h3>WHAT PARTS DO WE USE?</h3>
    <p>WE ONLY USE HIGH QUALITY OEM<br>EQUIVALENT PARTS.<br>WE USE ARDEN OR VELT SPARK<br>PLUGS, HIGH QUALITY FILTER &amp; PRE-<br>MIUM LONG LIFE OIL</p>
  </section>

  <p class="abs advice">expert advice...<br>&nbsp;in plain english</p>

  <address class="abs contact heavy">
    CONTACT US<br>01236 555014<br>SALES@BREMWICK.CO.UK<br>WWW.BREMWICK.CO.UK
  </address>

  <div class="abs badge badge-one" role="img" aria-label="Authorised testing facility badge"></div>
  <div class="abs badge badge-two" role="img" aria-label="Code of practice membership badge"></div>

  <footer class="abs address-band heavy">14-B HARROWFIELD PLACE | DUNMOOR PARK | KELVINBRAE | KB4 9QZ</footer>
</main>
</body>
</html>
```